Lavoie Roofing

Want a professional looking business card

Industry/Entity Type

Business

Contact Information for Business Card

Mark Lavoie ( Owner) mark@lavoieroofing.example, www.lavoieroofing.example, Adress: 4712 County road 31 Brookvale,ON X0A1B2

```html
<!DOCTYPE html>
<html lang="en">
<head>
<meta charset="utf-8">
<title>Lavoie Roofing – Business Card</title>
<link rel="stylesheet" href="https://fonts.googleapis.com/css2?family=Montserrat:wght@400;600;700&family=Open+Sans:wght@400;600&display=swap">
<style>
  :root {
    --brand-blue: #1f3f8c;
    --brand-blue-deep: #27398a;
    --ink-gray: #6b6b6b;
    --strip-gray: #8a8a8a;
    --paper: #ffffff;
    --backdrop: #d6d6d6;
  }
  * { box-sizing: border-box; margin: 0; padding: 0; }
  html, body {
    width: 1200px; height: 800px; overflow: hidden;
    background: var(--backdrop);
  }
  .canvas {
    width: 1200px; height: 800px;
    display: flex; flex-direction: column; align-items: center; justify-content: center;
    gap: 32px;
  }
  .card {
    position: relative;
    width: 620px; height: 354px;
    overflow: hidden;
    box-shadow: 0 6px 18px rgba(0,0,0,.18);
  }

  /* Front side */
  .card-front { background: var(--paper); }
  .name-block {
    position: absolute; left: 0; top: 128px;
    padding-left: 42px;
  }
  .name-marker {
    position: absolute; left: 0; top: 4px;
    width: 14px; height: 34px; background: var(--brand-blue);
  }
  .person-name {
    font-family: "Montserrat", sans-serif; font-weight: 700;
    font-size: 20px; letter-spacing: .3px; color: var(--brand-blue);
    white-space: nowrap;
  }
  .person-role {
    font-family: "Open Sans", sans-serif; font-size: 14px;
    color: var(--ink-gray); margin-top: 2px;
  }
  .contact-block {
    position: absolute; left: 42px; top: 206px;
    font-family: "Open Sans", sans-serif; font-size: 13px;
    color: var(--ink-gray); line-height: 1.4;
  }
  .address { margin-bottom: 10px; }
  .contact-list { list-style: none; }
  .contact-list li { display: flex; align-items: center; gap: 10px; white-space: nowrap; }
  .contact-list svg { width: 13px; height: 13px; fill: var(--brand-blue); flex: none; }
  .contact-list .web { color: var(--brand-blue); }
  .brand-lockup {
    position: absolute; right: 40px; top: 120px;
    display: flex; align-items: center; gap: 10px;
    white-space: nowrap;
  }
  .brand-square { width: 16px; height: 16px; background: var(--brand-blue); flex: none; }
  .brand-name {
    font-family: "Montserrat", sans-serif; font-weight: 700;
    font-size: 26px; letter-spacing: 1px; color: var(--brand-blue);
    white-space: nowrap;
  }
  .bottom-band {
    position: absolute; left: 0; bottom: 0; width: 76%; height: 10px;
    background: var(--brand-blue);
  }
  .bottom-band-gray {
    position: absolute; right: 0; bottom: 0; width: 24%; height: 18px;
    background: var(--strip-gray);
  }

  /* Back side */
  .card-back {
    background: linear-gradient(135deg, var(--brand-blue) 0%, var(--brand-blue-deep) 100%);
  }
  .card-back .brand-lockup {
    right: auto; left: 50%; top: 150px; transform: translateX(-50%);
  }
  .card-back .brand-square { background: var(--paper); width: 18px; height: 18px; }
  .card-back .brand-name { color: var(--paper); font-size: 34px; }
  .back-web {
    position: absolute; left: 0; right: 0; bottom: 40px; text-align: center;
    font-family: "Open Sans", sans-serif; font-size: 13px; color: var(--paper);
  }
</style>
</head>
<body>
<main class="canvas">
  <section class="card card-front">
    <div class="name-block">
      <span class="name-marker"></span>
      <div class="person-name">MARK LAVOIE</div>
      <div class="person-role">OWNER</div>
    </div>
    <div class="contact-block">
      <p class="address">4712 County road 31<br>Brookvale,ON X0A1B2</p>
      <ul class="contact-list">
        <li>
          <svg viewBox="0 0 24 24" aria-hidden="true"><path d="M6.6 10.8a15.1 15.1 0 0 0 6.6 6.6l2.2-2.2a1 1 0 0 1 1-.25 11.4 11.4 0 0 0 3.6.57 1 1 0 0 1 1 1V20a1 1 0 0 1-1 1A17 17 0 0 1 3 4a1 1 0 0 1 1-1h3.5a1 1 0 0 1 1 1c0 1.25.2 2.45.57 3.57a1 1 0 0 1-.25 1z"/></svg>
          (000)555-0142
        </li>
        <li>
          <svg viewBox="0 0 24 24" aria-hidden="true"><path d="M2 5h20v14H2zM4 7v.5l8 5 8-5V7l-8 5z"/></svg>
          mark@lavoieroofing.example
        </li>
        <li class="web">
          <svg viewBox="0 0 24 24" aria-hidden="true"><path d="M12 2a10 10 0 1 0 0 20 10 10 0 0 0 0-20zm6.9 6h-3a15 15 0 0 0-1.3-3.9A8 8 0 0 1 18.9 8zM12 4c.8 1.2 1.5 2.5 1.9 4h-3.8C10.5 6.5 11.2 5.2 12 4zM4.3 14a8 8 0 0 1 0-4h3.4a16 16 0 0 0 0 4zm.8 2h3a15 15 0 0 0 1.3 3.9A8 8 0 0 1 5.1 16zm3-8h-3a8 8 0 0 1 4.3-3.9A15 15 0 0 0 8.1 8zM12 20c-.8-1.2-1.5-2.5-1.9-4h3.8c-.4 1.5-1.1 2.8-1.9 4zm2.3-6H9.7a14 14 0 0 1 0-4h4.6a14 14 0 0 1 0 4zm.3 5.9a15 15 0 0 0 1.3-3.9h3a8 8 0 0 1-4.3 3.9zm1.7-5.9a16 16 0 0 0 0-4h3.4a8 8 0 0 1 0 4z"/></svg>
          www.lavoieroofing.example
        </li>
      </ul>
    </div>
    <div class="brand-lockup">
      <span class="brand-square"></span>
      <span class="brand-name">LAVOIE ROOFING</span>
    </div>
    <span class="bottom-band"></span>
    <span class="bottom-band-gray"></span>
  </section>

  <section class="card card-back">
    <div class="brand-lockup">
      <span class="brand-square"></span>
      <span class="brand-name">LAVOIE ROOFING</span>
    </div>
    <p class="back-web">www.lavoieroofing.example</p>
  </section>
</main>
</body>
</html>
```